Stationary Design using supplied logo

24 Hour Completion required after acceptance

Business Cards
Letter Head
With Compliments Slips
Web Page Theme

Please only use a the following colors:

Red
Charcoal
Chrome/Silver
White

Red being the DOMINANT Color

Please email questions you may have.

Continued work available to suitably motivated designer.

Industry/Entity Type

Business

```html
<!DOCTYPE html>
<html lang="en">
<head>
<meta charset="utf-8">
<title>go capital – Business Card</title>
<link rel="stylesheet" href="https://fonts.googleapis.com/css2?family=Tinos&family=Arimo:ital,wght@0,400;1,400;1,700&display=swap">
<style>
  :root {
    --charcoal-deep: #141414;
    --charcoal: #1e1e1e;
    --charcoal-band: #2b2b2b;
    --red: #c8202f;
    --silver-light: #8a8a8a;
    --silver-dark: #3a3a3a;
    --white: #ffffff;
    --ink: #1a1a1a;
  }
  html, body {
    margin: 0;
    padding: 0;
    width: 1200px;
    height: 695px;
    overflow: hidden;
    background: var(--charcoal-deep);
  }
  .card {
    position: relative;
    width: 1200px;
    height: 695px;
    overflow: hidden;
    background: radial-gradient(ellipse at 40% 30%, var(--charcoal) 0%, var(--charcoal-deep) 80%);
    font-family: "Arimo", Arial, sans-serif;
    color: var(--white);
  }
  .card__bands {
    position: absolute;
    inset: 0;
  }
  .corner-fold {
    position: absolute;
    left: 0;
    top: 0;
  }
  .brand-band {
    position: absolute;
    left: 0;
    top: 23px;
    width: 705px;
    height: 139px;
    background: var(--red);
  }
  .brand-band__name {
    position: absolute;
    left: 200px;
    top: 22px;
    margin: 0;
    font-family: "Arimo", Arial, sans-serif;
    font-weight: 400;
    font-size: 64px;
    line-height: 1;
    color: var(--white);
    white-space: nowrap;
  }
  .brand-band__role {
    position: absolute;
    left: 202px;
    top: 98px;
    margin: 0;
    font-size: 22px;
    line-height: 1;
    color: var(--ink);
    white-space: nowrap;
  }
  .identity {
    position: absolute;
    left: 393px;
    width: 771px;
    top: 318px;
    text-align: center;
  }
  .identity__name {
    margin: 0;
    font-family: "Tinos", "Times New Roman", serif;
    font-weight: 400;
    font-size: 80px;
    line-height: 1;
  }
  .identity__rule {
    height: 2px;
    margin: 8px 0 0;
    border: 0;
    background: var(--red);
  }
  .identity__title {
    margin: 14px 0 0;
    font-style: italic;
    font-size: 40px;
    line-height: 1;
  }
  .contact {
    position: absolute;
    left: 383px;
    top: 528px;
    margin: 0;
  }
  .contact__row {
    display: flex;
    align-items: baseline;
    height: 38px;
    white-space: nowrap;
  }
  .contact__label {
    font-size: 30px;
  }
  .contact__value {
    margin: 0;
    font-style: italic;
    font-weight: 700;
  }
  .contact__value--address {
    margin-left: 16px;
    font-size: 19px;
  }
  .contact__value--email {
    margin-left: 14px;
    font-weight: 400;
    font-size: 23px;
  }
  .contact__value--mobile {
    margin-left: 20px;
    font-size: 22px;
  }
</style>
</head>
<body>
  <main class="card">
    <svg class="card__bands" width="1200" height="695" viewBox="0 0 1200 695" aria-hidden="true">
      <g fill="none" stroke="var(--charcoal-band)" opacity="0.85">
        <path d="M-60 230 C 300 140, 700 250, 1060 695" stroke-width="70"/>
        <path d="M-60 360 C 260 250, 640 330, 960 695" stroke-width="55"/>
        <path d="M300 140 C 620 140, 980 330, 1200 560" stroke-width="48"/>
        <path d="M500 150 C 800 170, 1080 290, 1240 420" stroke-width="40"/>
      </g>
    </svg>

    <div class="brand-band">
      <h1 class="brand-band__name">go capital</h1>
      <p class="brand-band__role">Chief Executive Officer</p>
    </div>

    <svg class="corner-fold" width="215" height="172" viewBox="0 0 215 172" aria-hidden="true">
      <defs>
        <linearGradient id="fold-silver" x1="0" y1="0" x2="1" y2="1">
          <stop offset="0" stop-color="var(--silver-light)"/>
          <stop offset="1" stop-color="var(--silver-dark)"/>
        </linearGradient>
      </defs>
      <polygon points="0,0 213,0 0,170" fill="url(#fold-silver)"/>
    </svg>

    <section class="identity">
      <h2 class="identity__name">Your Name</h2>
      <hr class="identity__rule">
      <p class="identity__title">- Your Designation -</p>
    </section>

    <dl class="contact">
      <div class="contact__row">
        <dt class="contact__label">Adress:</dt>
        <dd class="contact__value contact__value--address">NORTHVALE IT SOLUTIONS UNIT 4 IInd FLOOR SEC9 RIVERTON</dd>
      </div>
      <div class="contact__row">
        <dt class="contact__label">Email:</dt>
        <dd class="contact__value contact__value--email">info@northvaleitsolutions.com</dd>
      </div>
      <div class="contact__row">
        <dt class="contact__label">Mobile:</dt>
        <dd class="contact__value contact__value--mobile">+91-800 000 1234, +91-9000012345</dd>
      </div>
    </dl>
  </main>
</body>
</html>
```